Futuristic but clean CD Cover Design

I need a CD Cover design for my next EP. The music is electronic pop. I am looking for something clean but futuristic with neon colors .Name of band: peopleASponiesName of Album: CeylonI have attached my logo.I have also attached CD covers of the color scheme and clean look I am looking for.Thanks

Industry/Entity Type

Film Production

Requirements
Must have
• A clean future look. The music is electronic pop.

```html
<!DOCTYPE html>
<html lang="en">
<head>
<meta charset="utf-8">
<title>Varmel – lanternSOkites</title>
<link rel="stylesheet" href="https://fonts.googleapis.com/css2?family=Michroma&family=Oswald:wght@300;400&display=swap">
<style>
  :root {
    --backdrop: #5d5c68;
    --cover-top: #2c2a48;
    --cover-bottom: #0c0b1c;
    --sphere-edge: #6a4fb0;
    --sphere-core: #27264a;
    --streak: #c65cc8;
    --title: #d9dbe8;
    --title-edge: #e57ad0;
    --band: #c23fbf;
    --mark: #c9a296;
  }
  html, body {
    margin: 0;
    width: 1200px;
    height: 923px;
    overflow: hidden;
    background: var(--backdrop);
  }
  .canvas {
    position: relative;
    width: 1200px;
    height: 923px;
  }
  .cover {
    position: absolute;
    left: 260px;
    top: 121px;
    width: 680px;
    height: 680px;
    overflow: hidden;
    background: linear-gradient(160deg, var(--cover-top) 0%, #1b1a33 50%, var(--cover-bottom) 100%);
  }
  .sphere {
    position: absolute;
    left: 75px;
    top: 65px;
    width: 530px;
    height: 530px;
    border-radius: 50%;
    background: radial-gradient(circle at 50% 45%, var(--sphere-core) 0%, #1f1e3c 62%, rgba(106,79,176,0.55) 96%, rgba(106,79,176,0) 100%);
    box-shadow: 0 0 0 1px rgba(106,79,176,0.45);
  }
  .streak {
    position: absolute;
    left: 0;
    top: 270px;
    width: 680px;
    height: 120px;
    background: radial-gradient(ellipse 50% 50% at 55% 50%, rgba(198,92,200,0.55) 0%, rgba(198,92,200,0.18) 55%, rgba(198,92,200,0) 100%);
  }
  .streak-line {
    position: absolute;
    left: 10px;
    top: 323px;
    width: 640px;
    height: 10px;
    transform: rotate(-1.5deg);
    background: linear-gradient(90deg, rgba(120,170,230,0) 0%, rgba(150,190,240,0.55) 30%, rgba(220,220,255,0.5) 70%, rgba(220,220,255,0) 100%);
    filter: blur(3px);
  }
  .album-title {
    position: absolute;
    left: 95px;
    top: 300px;
    width: 540px;
    margin: 0;
    font-family: "Michroma", sans-serif;
    font-weight: 400;
    font-size: 58px;
    letter-spacing: 10px;
    line-height: 1;
    color: var(--title);
    text-align: center;
    transform: rotate(-1.5deg);
    text-shadow: 1px 1px 0 var(--title-edge), 0 0 10px rgba(229,122,208,0.5);
  }
  .band-name {
    position: absolute;
    left: 0;
    top: 370px;
    width: 700px;
    margin: 0;
    font-family: "Oswald", sans-serif;
    font-weight: 300;
    font-size: 38px;
    color: var(--band);
    text-align: center;
    transform: rotate(-1deg);
  }
  .label-mark {
    position: absolute;
    right: 18px;
    bottom: 26px;
    display: flex;
    align-items: center;
    gap: 4px;
    font-family: "Oswald", sans-serif;
    font-weight: 400;
    font-size: 11px;
    color: var(--mark);
  }
  .label-dot {
    width: 7px;
    height: 7px;
    border-radius: 50%;
    background: var(--mark);
  }
</style>
</head>
<body>
<main class="canvas">
  <section class="cover">
    <div class="sphere" role="img" aria-label="Glowing purple wireframe globe of connected network lines"></div>
    <div class="streak"></div>
    <div class="streak-line"></div>
    <h1 class="album-title">VARMEL</h1>
    <p class="band-name">lanternSOkites</p>
    <div class="label-mark"><span class="label-dot"></span>lanternSOkites</div>
  </section>
</main>
</body>
</html>
```